Postcard Design

I have an accounting firm and I would like to increase my customer base by a postcard mailout/letter dropI want a design that is eye catching and uses my logo. I specialise in small to medium business and offer services for commercial accounting and business advisory. I also want to offer a discount for new clients.Previously I had my website updated and would like to stay with the theme

Industry/Entity Type

Business Consultant

Font styles to use
Serif

Colors
b667aa
d3a5cc

Requirements
Must have
• the post card needs to be arty to attract attention. also business like

```html
<!DOCTYPE html>
<html lang="en">
<head>
<meta charset="utf-8">
<title>Mirela Accounting Services – Postcard Back</title>
<link rel="stylesheet" href="https://fonts.googleapis.com/css2?family=PT+Sans:wght@400;700&display=swap">
<style>
  :root {
    --backdrop: #232122;
    --card: #ffffff;
    --ink: #3c3c3c;
    --ink-strong: #4a4a4a;
    --plum: #a459a3;
    --plum-soft: #b667aa;
    --rule: #7a7a7a;
  }
  html, body {
    margin: 0;
    padding: 0;
    width: 1200px;
    height: 900px;
    overflow: hidden;
    background: var(--backdrop);
    font-family: "PT Sans", Arial, sans-serif;
  }
  .postcard {
    position: absolute;
    left: 45px;
    top: 57px;
    width: 1110px;
    height: 786px;
    background: var(--card);
  }
  .return-block {
    position: absolute;
    left: 40px;
    top: 543px;
    width: 500px;
    transform-origin: top left;
    transform: rotate(-90deg);
    color: var(--ink);
    white-space: nowrap;
  }
  .return-block p { margin: 0; }
  .firm-name {
    font-size: 41px;
    font-weight: 700;
    line-height: 52px;
    color: var(--ink-strong);
    padding-left: 2px;
  }
  .address {
    font-size: 21px;
    line-height: 27px;
    padding-left: 67px;
  }
  .address + .address { padding-left: 88px; }
  .phone {
    font-size: 34px;
    line-height: 44px;
    color: var(--plum);
    padding-left: 90px;
    margin-top: 2px !important;
  }
  .website {
    font-size: 21px;
    font-weight: 700;
    line-height: 28px;
    color: var(--plum);
    padding-left: 45px;
  }
  .brand-dot {
    position: absolute;
    left: 38px;
    top: 550px;
    width: 190px;
    height: 190px;
  }
  .stamp-box {
    position: absolute;
    left: 941px;
    top: 33px;
    width: 135px;
    height: 150px;
    border: 1px solid var(--rule);
  }
  .address-line {
    position: absolute;
    left: 699px;
    width: 365px;
    height: 0;
    border-top: 1px solid var(--rule);
  }
  .line-1 { top: 348px; }
  .line-2 { top: 451px; }
  .line-3 { top: 540px; }
</style>
</head>
<body>
  <main class="postcard">
    <section class="return-block">
      <p class="firm-name">Mirela Accounting Services</p>
      <p class="address">Level 2, 48 Harbour Lane , Kestrel Bay</p>
      <p class="address">New South Wales Australia 2999</p>
      <p class="phone">Call : 02 5550 1947</p>
      <p class="website">www.mirelaaccountingservices.com</p>
    </section>

    <svg class="brand-dot" viewBox="0 0 190 190" aria-hidden="true">
      <circle cx="95" cy="95" r="92" fill="var(--plum-soft)"/>
    </svg>

    <div class="stamp-box" aria-label="Stamp area"></div>
    <div class="address-line line-1"></div>
    <div class="address-line line-2"></div>
    <div class="address-line line-3"></div>
  </main>
</body>
</html>
```